QUORLANET - IT SERVICE PROVIDERS - TriFold Flyer

Looking for Exclusive Professional look TriFold Flyer (A4) to tell:
- what we do?
- Why choose us?
- Our Services
- Our Products
- Address and Contact Detail
From Designer:
=================
Look and Feel
Graphics - Icons - Shapes - Amazing Layouts - Exclusive Fonts.
All the content will be provided.
Please send your portfolio to check..
Reason: till now no one has send there designs - have to extend to get the designs...
If no one interested to give - then i need to ask a refund... thanx
Those who accepted my project - plz let me know your delivery dates...
and about content - plz mention the Titles which i have mentioned in Brief and put Lipsum text, i will replace them...
What i m looking is Awesome Layout and Design - Using Shapes / Graphics / Fonts... content u put lipsum content and more content you will get it from www.tenvoramix.com...
About services and other stuff.... thanx
Reason: not even 4 designers have submitted there design out of 13 acceptance.
Kindly send me the best design so as to give lots of projects...
Reason: Looking for more creative and unique design
Target Market(s)
Dubai and GCC
IT comsultants
IT Service Providers
Advertising Agencies
Software Development Cos.
Industry/Entity Type
It Professional
Look and feel

```html
<!DOCTYPE html>
<html lang="en">
<head>
<meta charset="utf-8">
<title>QUORLANET – Trifold Cover Panel</title>
<link rel="stylesheet" href="https://fonts.googleapis.com/css2?family=Lato:wght@400;700;900&display=swap">
<style>
  :root {
    --page-bg: #ffffff;
    --brand-blue: #1f4fa3;
    --brand-blue-light: #2f66c4;
    --navy: #182c5e;
    --ring-navy: #112853;
    --accent-red: #5e1616;
    --panel-gray: #8e949b;
    --base-black: #1a1a1c;
    --text-white: #ffffff;
    --seg-teal: #3b8194;
    --seg-olive: #8d8a25;
    --seg-green: #3d9a3a;
    --seg-red: #8e1f1f;
  }
  html, body {
    margin: 0;
    padding: 0;
    width: 1081px;
    height: 1200px;
    overflow: hidden;
    background: var(--page-bg);
    font-family: "Lato", sans-serif;
  }
  .cover-panel {
    position: absolute;
    left: 270px;
    top: 30px;
    width: 540px;
    height: 1140px;
    background: var(--panel-gray);
    overflow: hidden;
    box-shadow: 0 6px 24px rgba(0,0,0,0.25);
  }
  .panel-bands {
    position: absolute;
    inset: 0;
    width: 540px;
    height: 1140px;
  }
  .brand-block {
    position: absolute;
    top: 58px;
    left: 0;
    width: 100%;
    text-align: center;
    color: var(--text-white);
  }
  .brand-name {
    font-weight: 900;
    font-size: 56px;
    letter-spacing: 2px;
    line-height: 1;
  }
  .brand-tagline {
    margin-top: 8px;
    font-size: 17px;
    letter-spacing: 8px;
    font-weight: 400;
  }
  .brand-rule {
    width: 370px;
    height: 1px;
    margin: 6px auto 0;
    background: var(--text-white);
    opacity: 0.8;
  }
  .brand-web {
    margin-top: 5px;
    font-size: 15px;
    letter-spacing: 7px;
  }
  .services-title {
    position: absolute;
    top: 420px;
    width: 100%;
    margin: 0;
    text-align: center;
    color: var(--text-white);
    font-size: 34px;
    font-weight: 400;
  }
  .services-wheel {
    position: absolute;
    left: 15px;
    top: 480px;
    width: 510px;
    height: 510px;
  }
  .ring-label, .seg-label {
    fill: var(--text-white);
    font-family: "Lato", sans-serif;
    text-anchor: middle;
    font-size: 18px;
  }
</style>
</head>
<body>
<main class="cover-panel">
  <svg class="panel-bands" viewBox="0 0 540 1140" aria-hidden="true">
    <defs>
      <linearGradient id="topBlue" x1="0" y1="0" x2="0" y2="1">
        <stop offset="0" stop-color="var(--brand-blue)"/>
        <stop offset="1" stop-color="var(--brand-blue-light)"/>
      </linearGradient>
    </defs>
    <polygon points="0,0 540,0 540,300 270,378 0,300" fill="var(--accent-red)"/>
    <polygon points="0,0 540,0 540,290 270,366 0,290" fill="var(--navy)"/>
    <polygon points="0,0 540,0 540,190 270,286 0,190" fill="url(#topBlue)"/>
    <polygon points="0,1000 270,1030 540,985 540,1140 0,1140" fill="var(--brand-blue)"/>
    <polygon points="0,1012 270,1040 540,997 540,1140 0,1140" fill="var(--navy)"/>
    <polygon points="0,1058 540,1040 540,1140 0,1140" fill="var(--brand-blue-light)"/>
    <polygon points="0,1066 540,1050 540,1140 0,1140" fill="var(--base-black)"/>
  </svg>

  <header class="brand-block">
    <div class="brand-name">QUORLANET</div>
    <div class="brand-tagline">IT SOLUTION PROVIDERS</div>
    <div class="brand-rule"></div>
    <div class="brand-web">www.quorlanet.com</div>
  </header>

  <h2 class="services-title">Solution &amp; Services</h2>

  <svg class="services-wheel" viewBox="-255 -255 510 510" role="img" aria-label="Wheel of services offered">
    <defs>
      <radialGradient id="gTeal" cx="0" cy="0" r="165" gradientUnits="userSpaceOnUse">
        <stop offset="0" stop-color="#0d1420"/><stop offset="1" stop-color="var(--seg-teal)"/>
      </radialGradient>
      <radialGradient id="gOlive" cx="0" cy="0" r="165" gradientUnits="userSpaceOnUse">
        <stop offset="0" stop-color="#151505"/><stop offset="1" stop-color="var(--seg-olive)"/>
      </radialGradient>
      <radialGradient id="gGreen" cx="0" cy="0" r="165" gradientUnits="userSpaceOnUse">
        <stop offset="0" stop-color="#081a08"/><stop offset="1" stop-color="var(--seg-green)"/>
      </radialGradient>
      <radialGradient id="gRed" cx="0" cy="0" r="165" gradientUnits="userSpaceOnUse">
        <stop offset="0" stop-color="#1a0505"/><stop offset="1" stop-color="var(--seg-red)"/>
      </radialGradient>
    </defs>
    <circle r="252" fill="var(--ring-navy)"/>
    <g stroke="#cfd6e4" stroke-width="1.5">
      <path d="M0 0 L-63.1 -152.4 A165 165 0 0 1 63.1 -152.4 Z" fill="url(#gTeal)"/>
      <path d="M0 0 L63.1 -152.4 A165 165 0 0 1 152.4 -63.1 Z" fill="url(#gOlive)"/>
      <path d="M0 0 L152.4 -63.1 A165 165 0 0 1 152.4 63.1 Z" fill="url(#gGreen)"/>
      <path d="M0 0 L152.4 63.1 A165 165 0 0 1 63.1 152.4 Z" fill="url(#gRed)"/>
      <path d="M0 0 L63.1 152.4 A165 165 0 0 1 -63.1 152.4 Z" fill="url(#gTeal)"/>
      <path d="M0 0 L-63.1 152.4 A165 165 0 0 1 -152.4 63.1 Z" fill="url(#gOlive)"/>
      <path d="M0 0 L-152.4 63.1 A165 165 0 0 1 -152.4 -63.1 Z" fill="url(#gGreen)"/>
      <path d="M0 0 L-152.4 -63.1 A165 165 0 0 1 -63.1 -152.4 Z" fill="url(#gRed)"/>
    </g>
    <circle r="10" fill="var(--ring-navy)" stroke="#cfd6e4" stroke-width="2"/>

    <g class="segment-labels">
      <text class="seg-label" x="0" y="-118">Mobile<tspan x="0" dy="21">Apps</tspan></text>
      <text class="seg-label" x="78" y="-84">B2C<tspan x="78" dy="21">Apps</tspan></text>
      <text class="seg-label" x="108" y="6">Branding</text>
      <text class="seg-label" x="80" y="68">Phone<tspan x="80" dy="21">Tablet</tspan></text>
      <text class="seg-label" x="0" y="110">Social<tspan x="0" dy="21">Apps</tspan></text>
      <text class="seg-label" x="-78" y="68">3D<tspan x="-78" dy="21">Modeling</tspan></text>
      <text class="seg-label" x="-104" y="6">Animation</text>
      <text class="seg-label" x="-78" y="-84">B2B<tspan x="-78" dy="21">Apps</tspan></text>
    </g>

    <g class="ring-labels">
      <text class="ring-label" x="0" y="-214">Web Design<tspan x="0" dy="21">Development</tspan></text>
      <text class="ring-label" transform="translate(148 -148) rotate(45)" y="-4">Enterprise<tspan x="0" dy="21">Application</tspan></text>
      <text class="ring-label" x="212" y="-4">Social<tspan x="212" dy="21">Media</tspan></text>
      <text class="ring-label" transform="translate(148 148) rotate(-45)" y="-4">Search Engine<tspan x="0" dy="21">Optimization</tspan></text>
      <text class="ring-label" x="0" y="198">IT Hardware<tspan x="0" dy="21">AMC</tspan></text>
      <text class="ring-label" transform="translate(-148 148) rotate(45)" y="-4">Database<tspan x="0" dy="21">Consultancy</tspan></text>
      <text class="ring-label" x="-212" y="-4">Print<tspan x="-212" dy="21">Media</tspan></text>
      <text class="ring-label" transform="translate(-148 -148) rotate(-45)" y="-4">Software<tspan x="0" dy="21">Development</tspan></text>
    </g>
  </svg>
</main>
</body>
</html>
```